Flier redesign

Sample fliers are attached from previous 2 years "Seasonal care 2018" and "2019 Seasonal Care" . Need an updated design for this year.

Possible images are attached to this brief. If you use the before/after pictures - you should use both of them. Use images attached to this brief or any from our website that you may prefer.

Colors

Designer to choose colors to be used in the design.

Requirements
Must have
• Colors should match our website theme. www.oakmerefieldgrounds.org
• Should be a "new" design, not just copying one of the prior year designs with a different image.
• Must be created in photoshop and file must be provided at the end.
• Text should be the same as 2019 version.

```html
<!DOCTYPE html>
<html lang="en">
<head>
<meta charset="utf-8">
<title>Oakmere Field Grounds – 2020 Landscaping Packages</title>
<link href="https://fonts.googleapis.com/css2?family=Montserrat:wght@500;600;700;800&family=Roboto:wght@400;500;700&family=Oswald:wght@400;500&display=swap" rel="stylesheet">
<style>
  :root{
    --maroon:#7a1c2c;
    --maroon-dark:#55101c;
    --charcoal:#444446;
    --ink:#333;
    --paper:#ffffff;
    --card-top:#ffffff;
    --card-bottom:#e2e2e2;
    --photo-sky:#cfd3d2;
    --photo-stone:#8c9190;
    --photo-grass:#6aa83a;
  }
  *{box-sizing:border-box;margin:0;padding:0}
  html,body{width:703px;height:1200px;overflow:hidden;background:var(--paper)}
  body{position:relative;font-family:'Roboto',sans-serif;color:var(--ink)}

  .masthead{position:absolute;top:0;left:0;width:703px;height:116px;display:flex;align-items:center;justify-content:center;gap:14px}
  .masthead .brand-word{font-family:'Montserrat',sans-serif;font-weight:600;font-size:24px;letter-spacing:1px;color:var(--maroon);text-transform:uppercase}
  .masthead .brand-dot{width:98px;height:72px;border-radius:50%;border:2px solid var(--charcoal);background:#f4f4f4}

  .hero{position:absolute;top:116px;left:0;width:703px;height:444px;border-radius:0 0 70px 70px;overflow:hidden;
    background:linear-gradient(180deg,var(--photo-sky) 0%,var(--photo-stone) 30%,#7f8784 48%,var(--photo-grass) 62%,#4f8a2a 100%)}
  .hero-title{position:absolute;left:129px;top:499px;width:452px;height:61px;background:var(--maroon);border-radius:28px 28px 0 0;
    display:flex;align-items:center;justify-content:center;gap:10px;color:#fff}
  .hero-title .year{font-family:'Montserrat',sans-serif;font-weight:800;font-size:31px}
  .hero-title .label{font-family:'Roboto',sans-serif;font-weight:500;font-size:25px;letter-spacing:.2px}

  .card{position:absolute;width:200px;display:flex;flex-direction:column;
    background:linear-gradient(180deg,var(--card-top) 0%,var(--card-bottom) 100%);
    border-radius:6px;box-shadow:0 4px 10px rgba(0,0,0,.22);padding:0 12px 36px 17px}
  .card.seasonal{left:30px;top:653px;height:437px}
  .card.basic{left:252px;top:619px;height:471px}
  .card.perpetual{left:475px;top:576px;height:489px}

  .ribbon{position:absolute;left:-10px;width:174px;background:var(--maroon);color:#fff;font-family:'Montserrat',sans-serif;
    font-weight:800;font-size:14px;line-height:13px;padding:8px 12px 8px 26px;border-radius:0 8px 8px 0;text-transform:uppercase}
  .ribbon::after{content:"";position:absolute;left:0;bottom:-8px;border-top:8px solid var(--maroon-dark);border-left:10px solid transparent}
  .card.seasonal .ribbon{top:37px}
  .card.basic .ribbon{top:42px}
  .card.perpetual .ribbon{top:28px;width:182px}

  .intro{font-family:'Montserrat',sans-serif;font-weight:500;font-size:12px;line-height:14px;color:var(--ink)}
  .card.seasonal .intro{margin-top:92px}
  .card.basic .intro{margin-top:126px}
  .card.perpetual .intro{margin-top:93px}

  .features{list-style:none;margin-top:14px}
  .card.basic .features{margin-top:22px}
  .features li{position:relative;padding-left:18px;font-size:11px;line-height:13px;margin-bottom:9px}
  .features li svg{position:absolute;left:0;top:1px;width:10px;height:10px}
  .features .accent{color:var(--maroon)}
  .features b{font-weight:500}

  .prices{margin-top:auto}
  .price-row{display:flex;align-items:center;justify-content:space-between;margin-top:9px}
  .price-label{font-family:'Montserrat',sans-serif;font-weight:700;font-size:11.5px;line-height:13px;color:var(--ink);text-transform:uppercase;white-space:nowrap}
  .price-tag{width:82px;height:30px;border:1.5px solid var(--maroon);border-radius:8px;display:flex;align-items:center;justify-content:center;
    color:var(--maroon);font-family:'Oswald',sans-serif;font-weight:500;font-size:24px;flex:none}
  .card.basic .price-tag,.card.perpetual .price-tag{width:76px}
  .price-tag sup{font-size:13px;margin-right:3px;position:relative;top:-3px}

  .note{margin-top:18px;font-size:10.5px;line-height:13px;color:var(--ink)}
  .note .accent{color:var(--maroon)}

  .footer{position:absolute;left:0;top:1105px;width:703px;height:95px}
  .footer svg.band{position:absolute;left:0;top:0}
  .contact{position:absolute;left:0;top:38px;width:703px;height:57px;display:flex;align-items:center;justify-content:center;gap:22px;color:#fff}
  .contact .item{display:flex;align-items:center;gap:8px;font-size:13px}
  .contact .phone{font-size:23px;font-weight:400}
  .contact svg{fill:#fff}
</style>
</head>
<body>

<header class="masthead">
  <span class="brand-word">Oakmere</span>
  <span class="brand-dot"></span>
  <span class="brand-word">Field Grounds</span>
</header>

<div class="hero" role="img" aria-label="Photograph of granite headstones with trimmed shrubs on a green cemetery lawn"></div>
<div class="hero-title"><span class="year">2020</span><span class="label">LANDSCAPING PACKAGES</span></div>

<svg width="0" height="0" style="position:absolute">
  <symbol id="tick" viewBox="0 0 10 10">
    <circle cx="5" cy="5" r="4.2" fill="none" stroke="#7a1c2c" stroke-width="1"/>
    <path d="M3 5.2 L4.5 6.6 L7.2 3.6" fill="none" stroke="#7a1c2c" stroke-width="1.1"/>
  </symbol>
</svg>

<section class="card seasonal">
  <h2 class="ribbon">Seasonal Care</h2>
  <p class="intro">Seasonal landscaping grave care.</p>
  <ul class="features">
    <li><svg><use href="#tick"/></svg>Weeding and trimming services on your gravesite approximately every 7 weeks during the growing <span class="accent">season:</span> <b>mid-April through mid-October</b></li>
  </ul>
  <div class="prices">
    <div class="price-row"><span class="price-label">3 Years</span><span class="price-tag"><sup>$</sup>345</span></div>
    <div class="price-row"><span class="price-label">2 Years</span><span class="price-tag"><sup>$</sup>230</span></div>
    <div class="price-row"><span class="price-label">1 Years</span><span class="price-tag"><sup>$</sup>115</span></div>
  </div>
  <p class="note">Multi-year payment locks in current rates.<span class="accent">Valid through 10/31/19.</span></p>
</section>

<section class="card basic">
  <h2 class="ribbon">Basic Careen Dowment</h2>
  <p class="intro">Landscaping care forever for graves with no plantings.</p>
  <ul class="features">
    <li><svg><use href="#tick"/></svg>Weeding and trimming services on your gravesite 2 times per year. <b>mid-May and mid-September</b></li>
    <li><svg><use href="#tick"/></svg>Monument leveling</li>
    <li><svg><use href="#tick"/></svg>Payment ensures grave</li>
  </ul>
  <div class="prices">
    <div class="price-row"><span class="price-label">12 Monthly<br>Payments of</span><span class="price-tag"><sup>$</sup>239</span></div>
  </div>
  <p class="note">Call for single payment discount.<br><span class="accent">Valid through 10/31/19</span></p>
</section>

<section class="card perpetual">
  <h2 class="ribbon">Perpetual Care Dowment</h2>
  <p class="intro">Landscaping care forever for graves with plantings.</p>
  <ul class="features">
    <li><svg><use href="#tick"/></svg>Weeding and triming services on your gravesite approximately every 7 weeks during the <span class="accent">growing season:</span> <b>mid-April through mid-October</b></li>
    <li><svg><use href="#tick"/></svg>Monument leveling and cleaning</li>
    <li><svg><use href="#tick"/></svg>Payment ensures grave care forever</li>
    <li><svg><use href="#tick"/></svg>Full bed of boxwood shrubs</li>
    <li><svg><use href="#tick"/></svg>Replacement of shrubs</li>
    <li><svg><use href="#tick"/></svg>Trust certificate</li>
  </ul>
  <div class="prices">
    <div class="price-row"><span class="price-label">12 Monthly<br>Payments of</span><span class="price-tag"><sup>$</sup>297</span></div>
  </div>
  <p class="note">Call for single payment discount.<br><span class="accent">Valid through 10/31/19</span></p>
</section>

<footer class="footer">
  <svg class="band" width="703" height="95" viewBox="0 0 703 95">
    <path d="M0 16 L640 16 Q700 14 703 -10 L703 95 L0 95 Z" fill="#7a1c2c"/>
    <path d="M0 95 Q12 42 80 38 L703 38 L703 95 Z" fill="#444446"/>
  </svg>
  <div class="contact">
    <span class="item phone">
      <svg width="20" height="20" viewBox="0 0 24 24"><path d="M6.6 10.8a15 15 0 0 0 6.6 6.6l2.2-2.2a1 1 0 0 1 1-.25 11.4 11.4 0 0 0 3.6.57 1 1 0 0 1 1 1V20a1 1 0 0 1-1 1A17 17 0 0 1 3 4a1 1 0 0 1 1-1h3.5a1 1 0 0 1 1 1c0 1.25.2 2.45.57 3.6a1 1 0 0 1-.25 1z"/></svg>
      (555) 214-0937
    </span>
    <span class="item">
      <svg width="12" height="12" viewBox="0 0 24 24"><circle cx="12" cy="12" r="10" fill="none" stroke="#fff" stroke-width="2.5"/><path d="M2 12h20M12 2c3 3 3 17 0 20M12 2c-3 3-3 17 0 20" fill="none" stroke="#fff" stroke-width="2"/></svg>
      www.oakmerefieldgrounds.org
    </span>
    <span class="item">
      <svg width="14" height="11" viewBox="0 0 24 18"><rect x="1" y="1" width="22" height="16" fill="none" stroke="#fff" stroke-width="2"/><path d="M1 1l11 9 11-9" fill="none" stroke="#fff" stroke-width="2"/></svg>
      info@oakmerefieldgrounds.org
    </span>
  </div>
</footer>

</body>
</html>
```